Rapidly growing regional logistics company looking for a modern clean website design.

We need a website for a 5 year old company based in New England.
We offer a complete logistics solution. With services dedicated to the changing economic environment. Services to our customers include, same day delivery, trucking and van service, warehouse & storage, pool distribution, and B2B installations.
We've implemented leading technology along the way, that provides visibility, accountability, up to the minute tracking, and project management.
Our goal to be known in the industry we service as an excellent provider of time-critical services and dependability.
Independently of the services we offer, our customers know that they can count on a true partner.

Target Market(s)

B2B, including printers, retail, manufacturers, wholesalers, electronics, any company that needs product delivered or warehoused

Industry/Entity Type

Logistics

Coding

Coded - Design and coding required

Number of Pages Required

5+ page

Font styles to use
Sans Serif

Colors
0255a3

Requirements
Must have
• Clean, modern design, limited clutter. Limited tabs, preferred everything on 1st screen roll down to see info

```html
<!DOCTYPE html>
<html lang="en">
<head>
<meta charset="utf-8">
<title>Merrow Logistics</title>
<link rel="stylesheet" href="https://fonts.googleapis.com/css2?family=Arimo:wght@400;700&display=swap">
<style>
:root{
  --ink:#1f1f1f;
  --body:#3a3530;
  --brand:#0255a3;
  --panel-bg:rgba(255,255,255,0.42);
  --panel-border:#6f7f94;
  --wood-light:#e9b378;
  --wood-mid:#d99451;
  --wood-dark:#c67a35;
  --button:#4caf50;
  --footer:#232b36;
  --white:#ffffff;
}
*{box-sizing:border-box;margin:0;padding:0}
html,body{width:1200px;height:675px;overflow:hidden;background:var(--white)}
body{font-family:"Arimo",Arial,sans-serif;color:var(--ink);position:relative}
.intro{position:absolute;left:0;top:0;width:1200px;height:132px;padding:0 14px;font-size:15px;line-height:20px;overflow:hidden}
.intro-lead{margin-top:-7px}
.intro-text{margin-top:16px;text-align:justify}
.feature-band{position:absolute;left:0;top:132px;width:1200px;height:402px;
  background:linear-gradient(135deg,var(--wood-light) 0%,var(--wood-mid) 30%,var(--wood-light) 55%,var(--wood-dark) 80%,var(--wood-mid) 100%)}
.panel{position:absolute;top:47px;width:336px;background:var(--panel-bg);border:1px solid var(--panel-border);
  padding:20px 10px 8px;text-align:center;overflow:hidden}
.panel:nth-child(1){left:48px;height:298px}
.panel:nth-child(2){left:432px;height:315px}
.panel:nth-child(3){left:816px;height:298px}
.panel-title{font-size:19px;font-weight:700;letter-spacing:1px;line-height:22px;color:var(--brand);margin-bottom:20px}
.panel-text{font-size:15px;line-height:20.8px;color:var(--body)}
.panel-text + .panel-text{margin-top:20px}
.top-button{position:absolute;left:540px;top:547px;width:120px;height:35px;background:var(--button);color:var(--white);
  font-size:12px;border:0;display:flex;align-items:center;justify-content:center;font-family:inherit}
.site-footer{position:absolute;left:0;top:619px;width:1200px;height:56px;background:var(--footer);color:var(--white);
  font-size:16px;display:flex;align-items:center;justify-content:center}
</style>
</head>
<body>
<section class="intro">
  <p class="intro-lead">Merrow Logistics moves freight across New England with same day delivery and dependable service.</p>
  <p class="intro-text">For five years Merrow Logistics has delivered a complete logistics solution for businesses across New England. Our services are built for a changing economic environment: same day delivery, trucking and van service, warehouse and storage, pool distribution and B2B installations. We serve printers, retailers, manufacturers, wholesalers and electronics firms, and any company that needs product delivered or warehoused. Leading technology gives every customer visibility, accountability, up to the minute tracking and project management on each job. Our goal is to be known across the industry we serve as an excellent provider of time-critical services and dependability, and our customers know they can count on a true partner every day.</p>
</section>

<section class="feature-band" role="img" aria-label="Background photo of warm oak parquet flooring">
  <article class="panel">
    <h2 class="panel-title">SAME DAY DELIVERY</h2>
    <p class="panel-text">When a shipment cannot wait, our drivers pick up and deliver within hours. Trucking and van service covers every state in New England, with routes planned around your deadlines. Pool distribution combines orders into one efficient run, lowering cost while keeping delivery windows tight. From printers to wholesalers, we keep product moving on time and in perfect condition.</p>
  </article>
  <article class="panel">
    <h2 class="panel-title">WAREHOUSE &amp; STORAGE</h2>
    <p class="panel-text">Secure, climate controlled space holds your inventory until the moment it is needed. Our team receives, stores, picks and packs orders with care, so retail and manufacturing clients can grow without the cost of their own building.</p>
    <p class="panel-text">B2B installations complete the job: we deliver, assemble and set up equipment right at your customer's door.</p>
  </article>
  <article class="panel">
    <h2 class="panel-title">LIVE TRACKING</h2>
    <p class="panel-text">Leading technology gives you full visibility from pickup to proof of delivery. Follow every load with up to the minute tracking, clear accountability at each stop and project management tools for larger jobs. Our dispatch team watches every route, so time-critical freight arrives when promised and you always know where it is.</p>
  </article>
</section>

<button class="top-button" type="button">Go to top</button>

<footer class="site-footer">© Merrow Logistics 2017.</footer>
</body>
</html>
```